Business Cards

Business card design for my company.
I would like the card's background colour to be black. You can also see our web site to get an idea of our brand. https://www.dlqmarrowfield.com.au/
- Name
- Email

```html
<!DOCTYPE html>
<html lang="en">
<head>
<meta charset="utf-8">
<title>DLQ Marrowfield – Business Cards</title>
<link rel="stylesheet" href="https://fonts.googleapis.com/css2?family=Montserrat:wght@400;500;700&display=swap">
<style>
  :root {
    --canvas: #2b2b2b;
    --card: #151515;
    --green: #1c9a4a;
    --white: #f2f2f2;
    --muted: #d6d6d6;
  }
  * { margin: 0; padding: 0; box-sizing: border-box; }
  html, body { width: 1200px; height: 900px; overflow: hidden; }
  body {
    background: var(--canvas);
    font-family: "Montserrat", sans-serif;
    color: var(--white);
    display: flex;
    flex-direction: column;
    align-items: center;
    justify-content: center;
    gap: 60px;
  }
  .card {
    width: 600px;
    height: 343px;
    background: var(--card);
    border-radius: 22px;
    box-shadow: 0 14px 30px rgba(0,0,0,.45);
    position: relative;
    overflow: hidden;
  }

  /* Front */
  .card--front {
    display: flex;
    align-items: center;
    justify-content: center;
  }
  .wordmark {
    display: flex;
    align-items: center;
    gap: 14px;
    font-weight: 700;
    color: var(--white);
    letter-spacing: .06em;
  }
  .wordmark__square {
    width: 18px; height: 18px;
    background: var(--green);
  }
  .card--front .wordmark { font-size: 40px; }

  /* Back */
  .card--back .wordmark {
    position: absolute;
    top: 48px;
    right: 46px;
    font-size: 24px;
    gap: 10px;
  }
  .card--back .wordmark__square { width: 12px; height: 12px; }
  .details {
    position: absolute;
    left: 46px;
    right: 40px;
    top: 150px;
    display: flex;
    align-items: flex-start;
  }
  .person { width: 230px; text-align: right; padding-right: 22px; }
  .person__name {
    color: var(--green);
    font-weight: 700;
    font-size: 27px;
    line-height: 1.1;
  }
  .person__title {
    font-size: 13px;
    color: var(--muted);
    margin-top: 6px;
  }
  .person__location {
    font-size: 13px;
    color: var(--muted);
    margin-top: 22px;
    white-space: nowrap;
  }
  .divider {
    width: 2px;
    height: 92px;
    background: var(--green);
    margin-top: 4px;
  }
  .contact {
    list-style: none;
    padding-left: 22px;
    font-size: 14px;
    color: var(--muted);
  }
  .contact li {
    display: flex;
    align-items: center;
    gap: 9px;
    height: 28px;
  }
  .contact svg { width: 13px; height: 13px; fill: var(--muted); flex: none; }
</style>
</head>
<body>
  <section class="card card--back" aria-label="Business card back">
    <div class="wordmark"><span class="wordmark__square"></span>DLQ MARROWFIELD</div>
    <div class="details">
      <div class="person">
        <div class="person__name">Owen Thackeray</div>
        <div class="person__title">General Manager</div>
        <div class="person__location">Marrow Bay, Tasmania, Australia</div>
      </div>
      <div class="divider"></div>
      <ul class="contact">
        <li>
          <svg viewBox="0 0 24 24" aria-hidden="true"><path d="M6.6 10.8a15 15 0 0 0 6.6 6.6l2.2-2.2c.3-.3.7-.4 1-.2 1.1.4 2.3.6 3.6.6.6 0 1 .4 1 1V20c0 .6-.4 1-1 1A17 17 0 0 1 3 4c0-.6.4-1 1-1h3.5c.6 0 1 .4 1 1 0 1.3.2 2.5.6 3.6.1.3 0 .7-.2 1z"/></svg>
          0400 555 182
        </li>
        <li>
          <svg viewBox="0 0 24 24" aria-hidden="true"><path d="M2 5h20v14H2z M2 5l10 8 10-8" fill="none" stroke="#d6d6d6" stroke-width="2"/></svg>
          info@dlqmarrowfield.com.au
        </li>
        <li>
          <svg viewBox="0 0 24 24" aria-hidden="true"><circle cx="12" cy="12" r="10" fill="none" stroke="#d6d6d6" stroke-width="2"/><path d="M2 12h20M12 2c3 3 3 17 0 20M12 2c-3 3-3 17 0 20" fill="none" stroke="#d6d6d6" stroke-width="1.6"/></svg>
          www.dlqmarrowfield.com.au
        </li>
      </ul>
    </div>
  </section>

  <section class="card card--front" aria-label="Business card front">
    <div class="wordmark"><span class="wordmark__square"></span>DLQ MARROWFIELD</div>
  </section>
</body>
</html>
```